Brindle Grass Services website design

We want to create a Sports turf website for our business Brindle Grass Services - we do sports turf management on sports fields around the Mackay region soccer rugby league softball fields etc from full turf management plans and maintenance to just supply and apply of turf management products and just supply of products with program we also do grounds facility maintenance at council facility's and grounds that require a higher level of care - we will up load our logos and fonts etc to assist with the colour pallet for the website - we will have to have a landing page a shop page with tabs a gallery tab along with a grants initiative and our coastals finest green tab also - our font for the txt is called ethnocentric
Updates

how do we open time for people to submit we have no one submitted

Industry/Entity Type

Turf

Coding

Coded - Design and coding required

Number of Pages Required

5+ page

Font styles to use
Other font styles liked:
• ethnocentric

Requirements
Must have
• I have mentioned some waffle in the description that should assist
Should not have
• anything not related

```html
<!DOCTYPE html>
<html lang="en">
<head>
<meta charset="utf-8">
<title>Brindle Grass Services</title>
<link href="https://fonts.googleapis.com/css2?family=Orbitron:wght@600;800&family=Poppins:wght@400;500;600&display=swap" rel="stylesheet">
<style>
:root{
  --green:#33b249;
  --green-dark:#1d8a34;
  --ink:#0b0d0b;
  --paper:#f4f5f3;
  --white:#ffffff;
  --text:#3a3f3a;
}
*{box-sizing:border-box;margin:0;padding:0}
html,body{width:1200px;height:3168px;overflow:hidden}
body{background:var(--paper);font-family:'Poppins',sans-serif;color:var(--text);position:relative}
.display{font-family:'Orbitron',sans-serif;font-weight:800;text-transform:uppercase;letter-spacing:1px}
.btn{display:inline-block;background:var(--green);color:var(--white);font-family:'Orbitron',sans-serif;font-weight:600;font-size:20px;letter-spacing:1px;padding:8px 22px;border-radius:4px;text-transform:uppercase}

/* header */
.site-nav{position:absolute;top:0;left:0;width:1200px;height:44px;background:rgba(5,8,5,.85);display:flex;align-items:center;justify-content:space-between;padding:0 36px;z-index:2}
.brand{font-family:'Orbitron',sans-serif;font-weight:800;font-size:18px;color:var(--white);text-transform:uppercase}
.menu{display:flex;gap:22px;align-items:center;font-family:'Orbitron',sans-serif;font-weight:600;font-size:12px;color:var(--white)}
.menu .btn{font-size:12px;padding:5px 12px}

/* hero */
.hero{position:absolute;top:0;left:0;width:1200px;height:668px;background:linear-gradient(180deg,#1d2a22 0%,#2e4a32 45%,#3f7a35 75%,#2b5a24 100%)}
.hero-copy{position:absolute;top:150px;left:100px;width:1000px;text-align:center;color:var(--white)}
.hero-copy h1{font-size:42px;line-height:62px}
.hero-copy p{font-size:15px;line-height:22px;margin:28px auto 22px;width:860px}

/* who */
.who{position:absolute;top:688px;left:40px;width:1120px;height:464px;border-radius:6px;overflow:hidden;background:linear-gradient(90deg,#2f8f2a 0%,#3fa234 40%,#5bb040 70%,#3f8a2e 100%)}
.who-copy{position:absolute;top:82px;left:96px;width:440px;color:var(--white)}
.who-copy h2{font-size:40px;margin-bottom:18px}
.who-copy p{font-size:14px;line-height:20px;margin-bottom:26px}

/* services */
.h-green{color:var(--green-dark);font-size:40px}
.what{position:absolute;top:1256px;left:56px;width:520px}
.what p{font-size:15px;line-height:22px;margin:18px 0 26px}
.tile{position:absolute;border-radius:4px;overflow:hidden}
.tile span{position:absolute;left:24px;bottom:16px;font-size:36px;color:var(--white)}
.soccer{top:1196px;left:608px;width:552px;height:396px;background:linear-gradient(160deg,#b8c4c8 0%,#5f9a48 30%,#3d8a34 70%,#2c6d26 100%)}
.rugby{top:1608px;left:40px;width:552px;height:388px;background:linear-gradient(180deg,#2a3a52 0%,#6a8a5a 35%,#3f8a34 65%,#2e6e28 100%)}
.softball{top:1608px;left:608px;width:552px;height:388px;background:linear-gradient(180deg,#6f8c3f 0%,#8a6a44 40%,#4a9a3a 70%,#2e7028 100%)}

/* projects */
.projects{position:absolute;top:2084px;left:40px;width:260px}
.projects p{font-size:14px;line-height:20px;margin:14px 0 24px}
.projects .btn{width:220px;text-align:center}
.proj1{top:2040px;left:320px;width:370px;height:364px;background:linear-gradient(180deg,#7fb1d6 0%,#a7bfa0 35%,#4a9a3c 60%,#2f7b2a 100%)}
.proj2{top:2040px;left:704px;width:456px;height:364px;background:linear-gradient(180deg,#5a7a4a 0%,#3d6e32 40%,#3c8c34 70%,#2b6a26 100%)}
.dots{position:absolute;top:2370px;left:1092px;display:flex;gap:8px}
.dots i{width:10px;height:10px;border-radius:50%;background:rgba(255,255,255,.6)}
.dots i:first-child{background:var(--white)}

/* contact */
.contact{position:absolute;top:2448px;left:40px;width:1120px;height:476px;border-radius:6px;overflow:hidden;background:linear-gradient(160deg,#30402f 0%,#3e6a32 40%,#2f5a27 70%,#1e3a1a 100%)}
.contact h2{position:absolute;top:26px;width:100%;text-align:center;color:var(--white);font-size:32px}
.form{position:absolute;top:108px;left:176px;width:420px}
.field{height:36px;background:rgba(15,18,15,.85);border-radius:3px;margin-bottom:16px;color:#bfc4bf;font-size:13px;padding:9px 14px}
.form .btn{margin-top:4px;font-size:18px;padding:6px 30px}
.info{position:absolute;top:108px;left:660px;color:var(--white);font-size:16px}
.info li{list-style:none;display:flex;align-items:center;gap:12px;margin-bottom:34px}
.ico{width:34px;height:34px;flex:none}

/* footer */
.site-footer{position:absolute;top:2940px;left:0;width:1200px;height:228px;background:var(--ink);color:var(--white)}
.f-brand{position:absolute;top:32px;left:40px}
.f-brand .brand{font-size:20px;color:var(--green)}
.f-brand small{display:block;font-size:11px;color:#cfd4cf;margin-top:4px;letter-spacing:2px;text-transform:uppercase}
.socials{position:absolute;top:92px;left:40px;display:flex;gap:12px}
.socials i{width:32px;height:32px;border-radius:50%;background:var(--green)}
.copy{position:absolute;bottom:18px;left:40px;font-size:12px;color:#bfc4bf}
.f-col h4{font-family:'Orbitron',sans-serif;font-size:16px;margin-bottom:14px}
.f-col li{list-style:none;font-size:12px;margin-bottom:10px;display:flex;align-items:center;gap:8px}
.f-col svg{width:14px;height:14px;flex:none}
.links{position:absolute;top:36px;left:560px}
.f-contact{position:absolute;top:36px;left:952px}
</style>
</head>
<body>

<header class="site-nav">
  <div class="brand">Brindle Grass Services</div>
  <nav class="menu">
    <span>HOME</span><span>SERVICES</span><span>GALLERY</span><span>PRODUCTS</span><span>ABOUT US</span>
    <span class="btn">Contact Us</span>
  </nav>
</header>

<section class="hero" role="img" aria-label="Floodlit stadium with a freshly mown sports field">
  <div class="hero-copy">
    <h1 class="display">Sports turf management on sports fields around the Mackay region soccer rugby league softball fields etc</h1>
    <p>Sports field construction and maintenance involves designing, building, and preserving athletic surfaces for long-term performance, including earthworks, drainage, turf installation, irrigation, surface marking, and ongoing care to meet sporting codes and safety standards.</p>
    <span class="btn">Contact Us</span>
  </div>
</section>

<section class="who" role="img" aria-label="Groundsman mowing stripes into a green sports field">
  <div class="who-copy">
    <h2 class="display">Who We Are</h2>
    <p>Lorem ipsum dolor sit amet, consectetur adipiscing elit, sed do eiusmod tempor incididunt ut labore et dolore magna aliqua. Quis ipsum suspendisse ultrices gravida. Risus commodo viverra maecenas accumsan lacus vel facilisis.</p>
    <span class="btn">Learn More</span>
  </div>
</section>

<section class="what">
  <h2 class="display h-green">What We Do</h2>
  <p>Lorem ipsum dolor sit amet, consectetur adipiscing elit, sed do eiusmod tempor incididunt ut labore et dolore magna aliqua. Quis ipsum suspendisse ultrices gravida. Risus commodo viverra maecenas accumsan lacus vel facilisis.</p>
  <span class="btn">Learn More</span>
</section>

<div class="tile soccer" role="img" aria-label="Marked soccer field beside a grandstand"><span class="display">Soccer Field</span></div>
<div class="tile rugby" role="img" aria-label="Rugby field inside a full stadium"><span class="display">Rugby Field</span></div>
<div class="tile softball" role="img" aria-label="Softball diamond with clay infield"><span class="display">Softball Field</span></div>

<section class="projects">
  <h2 class="display h-green" style="font-size:34px;line-height:42px">Our Projects</h2>
  <p>Lorem ipsum dolor sit amet, consectetur adipiscing elit, sed do eiusmod tempor incididunt ut labore et dolore.</p>
  <span class="btn">View All</span>
</section>
<div class="tile proj1" role="img" aria-label="Newly lined sports oval with clubhouse"><span class="display">Project<br>Title</span></div>
<div class="tile proj2" role="img" aria-label="Irrigation sprinklers watering a field with a turf vehicle"><span class="display">Project<br>Title</span></div>
<div class="dots"><i></i><i></i><i></i></div>

<section class="contact" role="img" aria-label="Aerial view of a striped field with painted emblem">
  <h2 class="display">Contact</h2>
  <div class="form">
    <div class="field">Name</div>
    <div class="field">Tel No.</div>
    <div class="field">Email</div>
    <div class="field">Message</div>
    <span class="btn">Send</span>
  </div>
  <ul class="info">
    <li><svg class="ico" viewBox="0 0 34 34"><circle cx="17" cy="17" r="17" fill="#fff"/><path d="M12 9l3 0 1.5 4-2 1.5a9 9 0 0 0 5 5l1.5-2 4 1.5v3a2 2 0 0 1-2 2A14 14 0 0 1 10 11a2 2 0 0 1 2-2z" fill="#1d8a34"/></svg>07 4900 0000</li>
    <li><svg class="ico" viewBox="0 0 34 34"><circle cx="17" cy="17" r="17" fill="#fff"/></svg>/brindlegrassservices</li>
    <li><svg class="ico" viewBox="0 0 34 34"><circle cx="17" cy="17" r="17" fill="#fff"/><rect x="9" y="11" width="16" height="12" rx="1" fill="none" stroke="#1d8a34" stroke-width="2"/><path d="M9 12l8 6 8-6" fill="none" stroke="#1d8a34" stroke-width="2"/></svg>sales@brindlegrass.example</li>
  </ul>
</section>

<footer class="site-footer">
  <div class="f-brand"><span class="brand">Brindle Grass Services</span><small>coastals finest green</small></div>
  <div class="socials"><i></i><i></i><i></i></div>
  <div class="copy">© 2025 Brindle Grass Services</div>
  <div class="f-col links">
    <h4>LINKS</h4>
    <ul><li>SERVICES</li><li>GALLERY</li><li>PRODUCTS</li><li>ABOUT US</li></ul>
  </div>
  <div class="f-col f-contact">
    <h4>CONTACT</h4>
    <ul>
      <li><svg viewBox="0 0 14 14"><path d="M7 1a4 4 0 0 1 4 4c0 3-4 8-4 8S3 8 3 5a4 4 0 0 1 4-4z" fill="#33b249"/><circle cx="7" cy="5" r="1.5" fill="#0b0d0b"/></svg>Harbour Rise, QLD, Australia</li>
      <li><svg viewBox="0 0 14 14"><path d="M3 1h2.5l1 3-1.5 1a6 6 0 0 0 4 4l1-1.5 3 1V11a1.5 1.5 0 0 1-1.5 1.5A10 10 0 0 1 1.5 2.5 1.5 1.5 0 0 1 3 1z" fill="#33b249"/></svg>07 4900 0000</li>
      <li><svg viewBox="0 0 14 14"><rect x="1" y="3" width="12" height="8" fill="none" stroke="#33b249" stroke-width="1.4"/><path d="M1 3.5l6 4 6-4" fill="none" stroke="#33b249" stroke-width="1.4"/></svg>sales@brindlegrass.example</li>
    </ul>
  </div>
</footer>

</body>
</html>
```